Tulven Electrics Flyer Design Advertising

I am after an A5 Flyer design to help promote my electrical services business.
I would like to have information on what my business offers, photos of electrical work, and specials/deals for an amount of time.

Industry/Entity Type

Electrician

Font styles to use
Sans Serif

Colors
0292cd
33a6d7
85cae6
3176b5
333333
1b1b1b
ffffff
5c5c5c
474747

Requirements
Must have
• Specialising in New homes, renovations and commercial projects
• Contact details:
• ph. 0437 619 458
• email admin@tulvenelectrics.example.au
• facebook TulvenElectrics
• Specials/Deals:
• 10% off all electrical services
• or
• Free LED downlights on installation
• *Terms conditions apply
• ALL RESIDENTIAL & COMMERCIAL ELECTRICAL SERVICES
• - New Home installations
• - Commercial projects
• - Shop fit outs
• - Renovations
• - Smoke Detectors
• - Air Conditioning and Ceiling Fans
• - Garden Lighting
• - Oven and Cooktop Installations
• - Power Point installation
• - LED lighting upgrades
• - Security Lighting
• - Switchboard upgrades
• - Test and Tag
• - Commercial Property
• - General Electrical Maintenance

```html
<!DOCTYPE html>
<html lang="en">
<head>
<meta charset="utf-8">
<title>Tulven Electrics Flyer</title>
<link href="https://fonts.googleapis.com/css2?family=Saira+Condensed:wght@600;700&family=Signika:wght@400;600;700&display=swap" rel="stylesheet">
<style>
  :root{
    --blue:#0292cd;
    --blue-mid:#33a6d7;
    --blue-light:#85cae6;
    --blue-deep:#3176b5;
    --ink:#333333;
    --ink-dark:#1b1b1b;
    --grey:#5c5c5c;
    --grey-mid:#474747;
    --white:#ffffff;
    --red:#e3161f;
    --paper:#f1f3f5;
    --stage:#4f93b0;
  }
  *{box-sizing:border-box;margin:0;padding:0}
  html,body{width:1122px;height:1200px;overflow:hidden;background:var(--stage)}
  body{font-family:'Signika',sans-serif;position:relative}
  .flyer{position:absolute;left:151px;top:20px;width:820px;height:1160px;background:var(--paper);overflow:hidden;box-shadow:0 10px 30px rgba(0,0,0,.25)}
  .hero-photo{position:absolute;left:0;top:0;width:820px;height:560px;
    background:linear-gradient(180deg,#5a6fa0 0%,#8a8fb4 35%,#c9a57a 60%,#4d5a3a 85%,#3f5130 100%)}
  .waves{position:absolute;left:0;top:0;width:820px;height:700px}
  .logo-panel{position:absolute;left:22px;top:22px;width:300px;height:150px;background:rgba(255,255,255,.85);border-radius:0 0 38px 0;display:flex;align-items:center;gap:14px;padding-left:20px}
  .logo-dot{width:96px;height:96px;border-radius:50%;background:var(--blue)}
  .logo-name{font-family:'Signika',sans-serif;font-weight:700;font-size:30px;line-height:1.05;color:var(--ink)}
  .photo-circle{position:absolute;border-radius:50%;border:7px solid var(--white);box-shadow:0 4px 10px rgba(0,0,0,.25)}
  .photo-kitchen{left:20px;top:250px;width:236px;height:236px;background:linear-gradient(160deg,#f4f6f7,#c9d3d6 55%,#7a8a6b)}
  .photo-dining{left:240px;top:360px;width:184px;height:184px;background:linear-gradient(170deg,#e9e6e1,#b9b0a4 55%,#4a3f36)}
  .headline{position:absolute;left:0;width:820px;top:570px;text-align:center;font-family:'Saira Condensed',sans-serif;font-weight:700;font-size:40px;line-height:1.05;color:var(--ink);text-transform:uppercase}
  .headline .lead{color:var(--blue);text-transform:none}
  .services{position:absolute;left:46px;top:680px;width:730px;height:268px;background:var(--blue);border-radius:24px;border:4px solid #d8dde0}
  .services-tab{position:absolute;left:40px;top:-4px;width:640px;height:48px;background:var(--white);border-radius:0 0 22px 22px;font-weight:600;font-size:25px;color:var(--blue);display:flex;align-items:center;padding-left:24px}
  .service-list{position:absolute;top:62px;list-style:none;color:var(--white);font-weight:600;font-size:18.5px;line-height:22px}
  .service-list li::before{content:"•";margin-right:10px}
  .col-left{left:48px}
  .col-right{left:380px;top:84px}
  .offer-end{position:absolute;right:44px;top:944px;background:var(--red);color:var(--white);font-size:13px;font-weight:600;padding:4px 12px;border-radius:0 0 6px 6px}
  .specials{position:absolute;left:0;top:972px;width:820px;height:72px}
  .specials-tag{position:absolute;left:22px;top:6px;width:156px;height:58px;background:var(--red);color:var(--white);font-weight:700;font-size:26px;display:flex;align-items:center;padding-left:26px;clip-path:polygon(0 0,88% 0,100% 50%,88% 100%,0 100%)}
  .deal{position:absolute;color:var(--red);font-weight:700;font-size:44px;line-height:44px}
  .deal small{display:block;font-size:21px;line-height:26px;font-weight:400;color:var(--ink)}
  .deal-percent{left:196px;top:0}
  .deal-led{left:450px;top:0}
  .or-badge{position:absolute;left:386px;top:12px;width:38px;height:38px;border-radius:50%;background:var(--red);color:var(--white);font-size:20px;display:flex;align-items:center;justify-content:center;border:3px solid #f7c8c8}
  .terms{position:absolute;left:700px;top:12px;font-size:8px;line-height:9px;color:var(--ink);text-align:center;width:40px}
  .footer{position:absolute;left:0;top:1050px;width:820px;height:110px;background:var(--ink)}
  .license{position:absolute;left:230px;top:-2px;width:340px;height:30px;background:var(--blue);color:var(--white);font-size:13.5px;font-style:italic;display:flex;align-items:center;justify-content:center;clip-path:polygon(0 0,100% 0,92% 100%,8% 100%)}
  .contacts{position:absolute;left:24px;top:48px;display:flex;align-items:center;gap:22px;color:var(--white);font-weight:600;font-size:19px}
  .contact{display:flex;align-items:center;gap:8px}
  .contact svg{width:30px;height:30px}
  .social-dot{width:28px;height:28px;border-radius:50%;border:2px solid var(--white)}
</style>
</head>
<body>
<main class="flyer">
  <div class="hero-photo" role="img" aria-label="Photo of a house at dusk with a lit outdoor patio and palm trees"></div>
  <svg class="waves" viewBox="0 0 820 700" aria-hidden="true">
    <path d="M0 330 C150 420 330 520 540 470 C660 445 760 470 820 520 L820 700 L0 700Z" fill="var(--blue-deep)"/>
    <path d="M0 350 C160 450 340 540 550 490 C670 462 770 490 820 540 L820 700 L0 700Z" fill="var(--blue)"/>
    <path d="M0 380 C170 480 350 560 560 515 C680 490 770 520 820 570 L820 700 L0 700Z" fill="var(--white)"/>
    <path d="M0 400 C180 500 360 575 570 535 C690 512 775 545 820 590 L820 700 L0 700Z" fill="var(--paper)"/>
  </svg>
  <div class="logo-panel">
    <div class="logo-dot"></div>
    <div class="logo-name">Tulven<br>Electrics</div>
  </div>
  <div class="photo-circle photo-kitchen" role="img" aria-label="Photo of a bright modern kitchen with pendant lights"></div>
  <div class="photo-circle photo-dining" role="img" aria-label="Photo of a kitchen island with bar stools"></div>

  <h1 class="headline"><span class="lead">Specialising In:</span> New Homes,<br>Renovations &amp; Commercial Projects</h1>

  <section class="services">
    <h2 class="services-tab">All Residential &amp; Commercial Electrical Services</h2>
    <ul class="service-list col-left">
      <li>New Home installations</li>
      <li>Commercial projects</li>
      <li>Shop fit outs</li>
      <li>Renovations</li>
      <li>Smoke Detectors</li>
      <li>Garden Lighting</li>
      <li>Oven and Cooktop Installations</li>
    </ul>
    <ul class="service-list col-right">
      <li>Power Point installation</li>
      <li>LED lighting upgrades</li>
      <li>Security Lighting</li>
      <li>Switchboard upgrades</li>
      <li>Test and Tag</li>
      <li>Commercial Property</li>
      <li>General Electrical Maintenance</li>
    </ul>
  </section>

  <div class="offer-end">Offers end 30/11/18</div>

  <section class="specials">
    <div class="specials-tag">Specials</div>
    <div class="deal deal-percent">10% off<small>all electrical services</small></div>
    <div class="or-badge">or</div>
    <div class="deal deal-led">Free LED<small>downlights on installation</small></div>
    <div class="terms">*Terms conditions apply</div>
  </section>

  <footer class="footer">
    <div class="license">license # 000 000 000, ABN # 000 000 0000</div>
    <div class="contacts">
      <div class="contact">
        <svg viewBox="0 0 30 30" aria-hidden="true"><circle cx="15" cy="15" r="13" fill="none" stroke="#fff" stroke-width="2"/><path d="M10 8c1-1 2-1 3 0l1.5 2.5c.5 1 0 1.8-.7 2.3l-.8.6c.8 1.8 2 3 3.6 3.8l.6-.8c.5-.7 1.3-1.2 2.3-.7L22 17c1 1 1 2 0 3-1.4 1.4-3 1.6-5 .5-3-1.6-5.8-4.4-7.4-7.4-1-2-.9-3.6.4-5.1z" fill="#fff"/></svg>
        0437 619 458
      </div>
      <div class="contact">
        <svg viewBox="0 0 30 30" aria-hidden="true"><circle cx="15" cy="15" r="13" fill="none" stroke="#fff" stroke-width="2"/><rect x="8" y="10" width="14" height="10" rx="1" fill="none" stroke="#fff" stroke-width="1.8"/><path d="M8 10l7 6 7-6" fill="none" stroke="#fff" stroke-width="1.8"/></svg>
        admin@tulvenelectrics.example.au
      </div>
      <div class="contact">
        <span class="social-dot"></span>
        TulvenElectrics
      </div>
    </div>
  </footer>
</main>
</body>
</html>
```